Marketing Online ENewsletter

HI there! Tidewell Studio are a local marketing agency in West Sussex who provide expert advice and service. The aim of this Enewsletter is to provide market information to people new to marketing and who are starting a business, inform them about company news and promote sales via inspirational marketing strategies - to be seen as a leader in the local market place.

Mailchimp
Image led with click though links.
Social media icons.
Forward to friend sharing link
High end stylist look for inspiration and advice.
Chatty and not techie!
Editable banner image - change photo and Title/comment.
Clean background.
Fully editable for one article design or multiple articles.
CTA info at bottom.
Slogan 'Mighty oaks from little acorns grow'
Updates

Hello, Please note this contest is for an Enewsletter online design for use in Mailchimp not a logo. I look forward to seeing your designs. Thank you

Target Market(s)

Business

Industry/Entity Type

Marketing

Logo Text

Tidewell Studio

Font styles to use
Serif
Sans Serif

Colors
0655a3

Requirements
Must have
• Upload to Mailchimp
editable for one or multiple articles
Refer a friend section
Clear Social Media icons
Logo - Attached
Nice to have
• Attached are some examples

```html
<!DOCTYPE html>
<html lang="en">
<head>
<meta charset="utf-8">
<title>Tidewell Studio – Newsletter</title>
<link rel="stylesheet" href="https://fonts.googleapis.com/css2?family=Jost:wght@400;500&family=Open+Sans:wght@400&display=swap">
<style>
  :root {
    --navy: #232a64;
    --gold: #fdd073;
    --white: #ffffff;
    --ink: #3d3d3d;
    --icon-grey: #4a4a4a;
    --footer-grey: #e6e6e6;
    --footer-text: #8a8a8a;
    --hero-light: #e3e8eb;
    --hero-mid: #c8c9c6;
    --hero-warm: #b9ab86;
    --display: "Jost", "Helvetica Neue", Arial, sans-serif;
    --body: "Open Sans", Arial, sans-serif;
  }
  html, body { margin: 0; padding: 0; overflow: hidden; background: var(--white); }
  .newsletter {
    position: relative;
    width: 856px;
    height: 1200px;
    overflow: hidden;
    background: var(--white);
    font-family: var(--body);
  }

  /* Hero banner */
  .hero { position: absolute; left: 0; top: 0; width: 856px; height: 442px; }
  .hero-photo {
    position: absolute; inset: 0;
    background: linear-gradient(170deg, var(--hero-light) 0%, var(--hero-mid) 55%, var(--hero-warm) 100%);
  }
  .brand {
    position: absolute; left: 40px; top: 34px;
    font-family: var(--display); font-weight: 500;
    font-size: 30px; letter-spacing: 1px; color: var(--navy);
    display: flex; align-items: center; gap: 10px;
  }
  .brand-mark { width: 12px; height: 12px; border-radius: 50%; background: var(--navy); }
  .headline-band {
    position: absolute; left: 0;
    font-family: var(--display); font-weight: 400;
    color: var(--white); font-size: 24px;
    padding-left: 65px; box-sizing: border-box;
    display: flex; align-items: center;
  }
  .headline-band--gold { top: 302px; width: 423px; height: 36px; background: var(--gold); }
  .headline-band--navy { top: 343px; width: 247px; height: 42px; background: var(--navy); }

  /* Greeting */
  .greeting { position: absolute; left: 0; top: 442px; width: 856px; height: 155px; }
  .greeting-title {
    position: absolute; left: 62px; top: 16px; margin: 0;
    font-family: var(--display); font-weight: 500; font-size: 21px; color: var(--navy);
  }
  .greeting-text {
    position: absolute; left: 58px; top: 62px; width: 455px; margin: 0;
    font-size: 9.6px; line-height: 13.8px; color: var(--ink);
  }
  .cta-button {
    position: absolute; left: 630px; top: 52px; width: 178px; height: 52px;
    background: var(--gold); color: var(--white); text-decoration: none;
    font-family: var(--display); font-size: 24px;
    display: flex; align-items: center; padding-left: 15px; box-sizing: border-box; gap: 22px;
  }

  /* Features */
  .features { position: absolute; left: 0; top: 597px; width: 856px; height: 235px; background: var(--navy); }
  .feature { position: absolute; top: 0; width: 230px; text-align: center; color: var(--white); }
  .feature--creativity { left: 43px; }
  .feature--convenience { left: 328px; }
  .feature--custom { left: 594px; }
  .feature-icon { display: block; margin: 21px auto 0; width: 60px; height: 60px; }
  .feature-title { margin: 15px 0 0; font-family: var(--display); font-weight: 400; font-size: 23px; }
  .feature-text { margin: 14px auto 0; width: 205px; font-size: 9.6px; line-height: 13.8px; }

  /* Social */
  .social { position: absolute; left: 0; top: 832px; width: 856px; height: 165px; text-align: center; }
  .social-title {
    margin: 30px 0 0; font-family: var(--display); font-weight: 400; font-size: 22px; color: var(--icon-grey);
  }
  .social-link {
    position: absolute; top: 72px; width: 64px; height: 64px; border-radius: 50%; background: var(--icon-grey);
  }

  /* Slogan / refer */
  .refer { position: absolute; left: 0; top: 997px; width: 856px; height: 92px; background: var(--gold); text-align: center; color: var(--white); font-family: var(--display); }
  .slogan { margin: 10px 0 0; font-size: 23px; font-weight: 400; }
  .refer-link { display: inline-block; margin-top: 5px; font-size: 23px; color: var(--white); text-decoration: none; }

  /* Footer */
  .footer { position: absolute; left: 0; top: 1089px; width: 856px; height: 111px; background: var(--footer-grey); text-align: right; color: var(--footer-text); }
  .disclaimer-title { position: absolute; right: 52px; top: 16px; margin: 0; font-size: 9px; }
  .disclaimer-text { position: absolute; right: 50px; top: 38px; width: 200px; margin: 0; font-size: 9px; line-height: 13px; }
</style>
</head>
<body>
<main class="newsletter">

  <header class="hero">
    <div class="hero-photo" role="img" aria-label="Banner photo: a cheerful group of colleagues raising coffee cups together in a bright office"></div>
    <div class="brand"><span>Tidewell Studio</span><span class="brand-mark"></span></div>
    <div class="headline-band headline-band--gold">Inspirational marketing strategies</div>
    <div class="headline-band headline-band--navy">for your business</div>
  </header>

  <section class="greeting">
    <h1 class="greeting-title">Reciever,</h1>
    <p class="greeting-text">Lorem ipsum dolor sit amet, consectetur adipiscing elit. Maecenas hendrerit lorem finibus arcu sodales, vehicula lobortis felis scelerisque. Vestibulum iaculis id tortor ut sollicitudin. Sed nec urna enim. Maecenas et pellentesque metus. Aliquam molestie, quam sed vestibulum molestie, massa ipsum malesuada ante, ut commodo est enim sit amet orci. Pellentesque eu massa dapibus, tristique ipsum quis, sodales lacus.</p>
    <a class="cta-button" href="#">Visit Page
      <svg width="26" height="36" viewBox="0 0 26 36"><polyline points="5,4 20,18 5,32" fill="none" stroke="#fff" stroke-width="6"/></svg>
    </a>
  </section>

  <section class="features">
    <div class="feature feature--creativity">
      <svg class="feature-icon" viewBox="0 0 60 60" fill="none" stroke="#fff" stroke-width="3">
        <path d="M22 40c0-6-7-9-7-18a15 15 0 0 1 30 0c0 9-7 12-7 18z"/>
        <line x1="23" y1="46" x2="37" y2="46"/><line x1="24" y1="51" x2="36" y2="51"/><line x1="27" y1="56" x2="33" y2="56"/>
        <line x1="30" y1="2" x2="30" y2="-2"/><line x1="8" y1="22" x2="2" y2="22"/><line x1="52" y1="22" x2="58" y2="22"/>
        <line x1="12" y1="6" x2="8" y2="2"/><line x1="48" y1="6" x2="52" y2="2"/>
        <path d="M26 38v-10l4 4 4-4v10"/>
      </svg>
      <h2 class="feature-title">Creativity</h2>
      <p class="feature-text">Lorem ipsum dolor sit amet, consectetur adipiscing elit. Maecenas hendrerit lorem finibus arcu sodales, vehicula lobortis felis scelerisque.</p>
    </div>
    <div class="feature feature--convenience">
      <svg class="feature-icon" viewBox="0 0 60 60">
        <path d="M30 4a16 16 0 0 1 16 16c0 12-16 30-16 30S14 32 14 20A16 16 0 0 1 30 4z" fill="none" stroke="#fff" stroke-width="3"/>
        <polygon points="30,12 32.4,17.6 38.5,18 33.8,22 35.3,28 30,24.7 24.7,28 26.2,22 21.5,18 27.6,17.6" fill="#fff"/>
        <rect x="18" y="53" width="24" height="5" rx="2.5" fill="#fff"/>
      </svg>
      <h2 class="feature-title">Convenience</h2>
      <p class="feature-text">Lorem ipsum dolor sit amet, consectetur adipiscing elit. Maecenas hendrerit lorem finibus arcu sodales, vehicula lobortis felis scelerisque.</p>
    </div>
    <div class="feature feature--custom">
      <svg class="feature-icon" viewBox="0 0 60 60">
        <path d="M6 52V6h50v46" fill="none" stroke="#fff" stroke-width="3"/>
        <line x1="6" y1="13" x2="56" y2="13" stroke="#fff" stroke-width="3"/>
        <g fill="#fff">
          <circle cx="30" cy="34" r="10"/>
          <rect x="27" y="20" width="6" height="28"/><rect x="16" y="31" width="28" height="6"/>
          <rect x="27" y="20" width="6" height="28" transform="rotate(45 30 34)"/><rect x="27" y="20" width="6" height="28" transform="rotate(-45 30 34)"/>
          <circle cx="47" cy="27" r="5"/>
        </g>
        <circle cx="30" cy="34" r="4" fill="#232a64"/>
      </svg>
      <h2 class="feature-title">Custom Design</h2>
      <p class="feature-text">Lorem ipsum dolor sit amet, consectetur adipiscing elit. Maecenas hendrerit lorem finibus arcu sodales, vehicula lobortis felis scelerisque.</p>
    </div>
  </section>

  <section class="social">
    <h2 class="social-title">Connect with Us</h2>
    <a class="social-link" href="#" style="left:253px" aria-label="Social network link 1"></a>
    <a class="social-link" href="#" style="left:345px" aria-label="Social network link 2"></a>
    <a class="social-link" href="#" style="left:440px" aria-label="Social network link 3"></a>
    <a class="social-link" href="#" style="left:532px;width:70px;height:70px;top:69px" aria-label="Social network link 4"></a>
  </section>

  <section class="refer">
    <p class="slogan">Mighty oaks from little acorns grow</p>
    <a class="refer-link" href="#">Tell a friend &rsaquo;</a>
  </section>

  <footer class="footer">
    <p class="disclaimer-title">Disclaimer</p>
    <p class="disclaimer-text">Lorem ipsum dolor sit amet, consectetur adipiscing elit. Mauris facilisis ullamcorper nunc in consequat. Duis ut pellentesque nibh.</p>
  </footer>

</main>
</body>
</html>
```